Skylark Air Works Logo

I need a website and logo for the parent company Skylark Air Works, which encompasses general aviation aircraft repair, small aircrat rental and flight school. The company is based in Lawrenceville, Georgia at the Brookhollow county airfield. A saying that can be incorporated somehere could be, "Quality flying is safe flying", "Safety in mind is no accident" ,. I need a website and logo.

The company started as a repair shop performing repairs and inspections on Halvorn, Tamsel, Korvane and Drexley general aviation aircraft, all models of single engine piston, multi engine piston, and single engine turboprop with an emphasis on Halvorn Solstice and AeroKite turbo prop aircraft. We have se=ince entered the aircraft rental and flight instruction market using the Korvane 418 ang Halvorn Ranger aircraft.

Number of Pages; I don't know. Maybe 5 ? A home page for Skylark Air Works, page for maintenance and repairs and a couple for the rental and school. The maintenance shop is busy, always has been. I need to get the rental and school advertised and busy.

I have a logo for the maintenance shop shirts, not for the school. I do not have the file. I paid a business locally to do that and print on the shirts. They have the file.

Target Market(s)

In our flight school rental fleet department, we are looking for persons wishing to obtain their private pilot license and continuing on into their commercial and instrument ratings. In the aircraft maintenance department, we are looking for new customers who want a better and more quality relationship with their aircraft maintenance provider who will give more detail and quality in the repairs with an emphasis on safety and fewer problems between scheduled maintenance cycles on their aircraft. Skylark's owner, Dale Fenwick, has been performing aircraft maintenance in the Atlanta area for 27 years. He has built a steady customer base through those years.

```html
<!DOCTYPE html>
<html lang="en">
<head>
<meta charset="utf-8">
<title>Skylark Aviation</title>
<link rel="stylesheet" href="https://fonts.googleapis.com/css2?family=Montserrat:wght@300;400;600;700;800&family=Roboto:wght@400;500;700&display=swap">
<style>
:root{
  --navy:#1c3883;
  --navy-deep:#142a6b;
  --blue:#0a8fd2;
  --sky:#1aa3e0;
  --ink:#2a2a2a;
  --text:#6e6e6e;
  --pale:#edf1f6;
  --dark:#272727;
  --white:#ffffff;
  --grad:linear-gradient(90deg,var(--navy) 0%,var(--blue) 100%);
}
*{margin:0;padding:0;box-sizing:border-box}
html,body{width:1200px;height:3953px;overflow:hidden}
body{position:relative;background:var(--white);font-family:'Roboto',sans-serif;color:var(--text)}
.abs{position:absolute}
.heading{font-family:'Montserrat',sans-serif;font-weight:800;color:var(--ink);letter-spacing:.5px;text-transform:uppercase}
.heading .light{font-weight:300;color:#555}
.btn{position:absolute;display:flex;align-items:center;justify-content:center;background:var(--grad);color:var(--white);font-family:'Roboto',sans-serif;font-weight:700;font-size:13px;border-radius:24px;text-transform:uppercase}
.para{font-size:14.5px;line-height:26.5px;color:var(--text);text-align:justify}
.para + .para{margin-top:10px}
.photo{position:absolute;overflow:hidden}

/* header */
.site-header{position:absolute;left:0;top:0;width:1200px;height:120px;background:var(--white)}
.brand{position:absolute;left:112px;top:48px;width:130px;text-align:center}
.brand-name{font-family:'Montserrat',sans-serif;font-weight:800;font-size:23px;color:var(--navy-deep);letter-spacing:.5px}
.brand-sub{font-family:'Montserrat',sans-serif;font-size:8px;letter-spacing:4px;color:#555;margin-top:2px}
.brand-mark{position:absolute;left:148px;top:14px;width:36px;height:36px;border-radius:50%;background:var(--grad)}
.nav{position:absolute;top:52px;left:362px;display:flex;font-family:'Montserrat',sans-serif;font-weight:600;font-size:14px;color:var(--ink)}
.nav span{margin-right:28px}
.nav .active{color:var(--blue)}
.social{position:absolute;display:flex;gap:8px}
.social span{width:34px;height:34px;border-radius:50%;border:2px solid var(--navy);color:var(--navy);font-family:'Roboto',sans-serif;font-weight:700;font-size:13px;display:flex;align-items:center;justify-content:center}

/* hero */
.hero-photo{left:0;top:120px;width:1200px;height:650px;background:linear-gradient(135deg,#8a96a3 0%,#c9d2dc 40%,#e6ebef 70%,#9aa5b2 100%)}
.hero-panel{position:absolute;left:112px;top:265px;width:486px;height:241px;background:rgba(255,255,255,.55);border-radius:18px}
.hero-title{position:absolute;left:164px;top:298px;font-family:'Montserrat',sans-serif;font-size:40px;line-height:48px;color:var(--ink)}
.hero-title b{font-weight:800}
.hero-title span{font-weight:400}
.arrow{position:absolute;width:36px;height:36px;border-radius:50%;background:var(--white);display:flex;align-items:center;justify-content:center}

/* image circles */
.ring{position:absolute;border-radius:50%}
.ring .photo{border-radius:50%}

/* services */
.services{left:0;top:1364px;width:1200px;height:648px;background:var(--pale)}
.card{position:absolute;top:1516px;width:307px;height:421px;background:var(--white);box-shadow:0 4px 14px rgba(0,0,0,.12)}
.card .photo{left:8px;top:8px;width:291px;height:203px}
.card-icon{position:absolute;left:113px;top:171px;width:80px;height:80px;border-radius:50%;background:var(--grad);border:5px solid var(--white);display:flex;align-items:center;justify-content:center}
.card h3{position:absolute;left:0;top:274px;width:307px;text-align:center;font-family:'Roboto',sans-serif;font-weight:500;font-size:17px;color:var(--ink)}
.card p{position:absolute;left:20px;top:308px;width:267px;text-align:center;font-size:13px;line-height:23px;color:var(--text)}
.card a{position:absolute;left:0;top:389px;width:307px;text-align:center;font-weight:700;font-size:12px;color:var(--blue);text-decoration:none}

/* clients */
.clients{left:0;top:2012px;width:1200px;height:325px;background:linear-gradient(90deg,var(--navy-deep) 0%,#1060b4 55%,var(--blue) 100%)}
.client{position:absolute;top:2161px;width:209px;height:101px;background:var(--white);border-radius:6px;display:flex;align-items:center;justify-content:center;font-family:'Montserrat',sans-serif;font-weight:700;font-size:26px;color:var(--navy)}

/* footer */
.footer{left:0;top:3530px;width:1200px;height:423px;background:var(--dark)}
.foot-title{position:absolute;top:3640px;font-family:'Roboto',sans-serif;font-weight:700;font-size:16px;color:var(--white)}
.foot-link{position:absolute;left:342px;font-size:14px;color:#ddd;display:flex;align-items:center;gap:18px}
.dot{width:12px;height:12px;border-radius:50%;background:var(--blue);display:inline-block}
.info{position:absolute;left:563px;font-size:11.5px;line-height:17px;color:#ddd}
.info b{display:block;font-size:14px;color:var(--white);font-weight:500;margin-bottom:4px}
</style>
</head>
<body>

<header class="site-header">
  <div class="brand-mark"></div>
  <div class="brand">
    <div class="brand-name">SKYLARK</div>
    <div class="brand-sub">AVIATION</div>
  </div>
  <nav class="nav"><span class="active">HOME</span><span>ABOUT US</span><span>SERVICES &#8964;</span><span>CONTACT</span></nav>
  <div class="btn" style="left:784px;top:38px;width:140px;height:45px;font-size:13px">Get a Quote</div>
  <div class="social" style="left:970px;top:43px"><span>N</span><span>C</span><span>W</span></div>
</header>

<!-- hero -->
<div class="photo hero-photo" role="img" aria-label="Two technicians reviewing a tablet beside a jet in a bright maintenance hangar"></div>
<div class="hero-panel"></div>
<h1 class="hero-title"><b>SAFETY IN MIND IS</b><br><span>NO ACCIDENT</span></h1>
<div class="btn" style="left:164px;top:422px;width:141px;height:43px">Get Started</div>
<div class="arrow" style="left:37px;top:401px"><svg width="12" height="12" viewBox="0 0 12 12"><path d="M8 1 3 6l5 5" fill="none" stroke="#222" stroke-width="2"/></svg></div>
<div class="arrow" style="left:1125px;top:401px"><svg width="12" height="12" viewBox="0 0 12 12"><path d="M4 1l5 5-5 5" fill="none" stroke="#222" stroke-width="2"/></svg></div>
<svg class="abs" style="left:0;top:600px" width="1200" height="180" viewBox="0 0 1200 180">
  <path d="M0,92 C260,20 480,40 600,100 C720,160 1000,165 1200,40 L1200,180 L0,180Z" fill="#fff"/>
  <path d="M0,92 C260,20 480,40 600,100" fill="none" stroke="#1c3883" stroke-width="9"/>
  <path d="M600,100 C720,160 1000,165 1200,40" fill="none" stroke="#0a8fd2" stroke-width="9"/>
  <circle cx="598" cy="106" r="48" fill="#fff" stroke="#e8eef4" stroke-width="4"/>
  <text x="598" y="110" text-anchor="middle" font-family="Montserrat, sans-serif" font-weight="800" font-size="12" fill="#1c3883">SKYLARK</text>
</svg>

<!-- about -->
<div class="ring" style="left:111px;top:814px;width:438px;height:438px;background:linear-gradient(135deg,var(--navy),var(--blue))">
  <div class="photo" style="left:26px;top:14px;width:406px;height:406px;background:linear-gradient(160deg,#5b6470,#b9c1ca 55%,#8a939d)" role="img" aria-label="Small aircraft parked inside a maintenance hangar"></div>
</div>
<h2 class="heading abs" style="left:600px;top:856px;font-size:40px">ABOUT <span class="light">US</span></h2>
<div class="abs" style="left:600px;top:926px;width:489px">
  <p class="para">Lorem ipsum dolor sit amet, consectetur adipiscing elit, sed do eiusmod tempor incididunt ut labore et dolore magna aliqua. Ut enim ad minim veniam, quis nostrud exercitation ullamco laboris nisi ut aliquip ex ea commodo conseute irure dolor in reprehea.</p>
  <p class="para">Consectetur adipiscing elit, sed do eiusmod tempor incididunt ut labore et dolore magna aliqua ut enim ad minim veniam, quis nostrud exer citation ullamco laboris nisi ut aliquip exea.</p>
</div>
<div class="btn" style="left:600px;top:1158px;width:134px;height:45px">Learn More</div>

<!-- services -->
<section class="abs services"></section>
<h2 class="heading abs" style="left:0;top:1432px;width:1200px;text-align:center;font-size:40px">OUR <span class="light">SERVICES</span></h2>

<div class="card" style="left:112px">
  <div class="photo" style="background:linear-gradient(135deg,#4a4f57,#a39a8e 60%,#6b6f76)" role="img" aria-label="Mechanic working on an aircraft engine"></div>
  <div class="card-icon"><svg width="34" height="34" viewBox="0 0 34 34" fill="none" stroke="#fff" stroke-width="2"><circle cx="17" cy="13" r="7"/><circle cx="17" cy="13" r="2.5"/><path d="M4 28h8l6-3h8"/></svg></div>
  <h3>MAINTENANCE &amp; REPAIRS</h3>
  <p>Sed ut perspiciatis unde omnis iste natus error sit voluptatem accusantium dolor emque laudantiumea.</p>
  <a>LEARN MORE &#10148;</a>
</div>
<div class="card" style="left:446px">
  <div class="photo" style="background:linear-gradient(135deg,#8b96a2,#dde3e8 55%,#9aa4ae)" role="img" aria-label="Small jet parked in a hangar"></div>
  <div class="card-icon"><svg width="34" height="34" viewBox="0 0 34 34" fill="none" stroke="#fff" stroke-width="2"><circle cx="17" cy="17" r="12"/><path d="M9 17h16M17 11v12"/></svg></div>
  <h3>SMALL AIRCRAFT RENTAL</h3>
  <p>Sed ut perspiciatis unde omnis iste natus error sit voluptatem accusantium dolor emque laudantiumea.</p>
  <a>LEARN MORE &#10148;</a>
</div>
<div class="card" style="left:781px">
  <div class="photo" style="background:linear-gradient(135deg,#7f9a6a,#c9d6c0 45%,#6e7b88)" role="img" aria-label="Two students seated in a flight simulator"></div>
  <div class="card-icon"><svg width="34" height="34" viewBox="0 0 34 34" fill="none" stroke="#fff" stroke-width="2"><circle cx="17" cy="17" r="12"/><path d="M10 19l14-6-4 9-3-3z"/></svg></div>
  <h3>FLIGHT SCHOOL</h3>
  <p>Sed ut perspiciatis unde omnis iste natus error sit voluptatem accusantium dolor emque laudantiumea.</p>
  <a>LEARN MORE &#10148;</a>
</div>

<!-- clients -->
<section class="abs clients"></section>
<h2 class="heading abs" style="left:0;top:2080px;width:1200px;text-align:center;font-size:40px;color:#fff">OUR <span class="light" style="color:#fff">CLIENTS</span></h2>
<div class="client" style="left:141px">Halvorn</div>
<div class="client" style="left:377px">Tamsel</div>
<div class="client" style="left:614px">Korvane</div>
<div class="client" style="left:850px">Drexley</div>

<!-- rental -->
<h2 class="heading abs" style="left:112px;top:2472px;font-size:40px">RENTAL</h2>
<div class="abs" style="left:112px;top:2545px;width:489px">
  <p class="para">Lorem ipsum dolor sit amet, consectetur adipiscing elit, sed do eiusmod tempor incididunt ut labore et dolore magna aliqua. Ut enim ad minim veniam, quis nostrud exercitation ullamco laboris nisi ut aliquip ex ea commodo conseute irure dolor in reprehea.</p>
  <p class="para">Consectetur adipiscing elit, sed do eiusmod tempor incididunt ut labore et dolore magna aliqua ut enim ad minim veniam, quis nostrud exer citation ullamco laboris nisi ut aliquip exea.</p>
</div>
<div class="btn" style="left:112px;top:2775px;width:134px;height:45px">Learn More</div>
<div class="ring" style="left:656px;top:2436px;width:432px;height:432px;background:linear-gradient(315deg,var(--blue),var(--navy))">
  <div class="photo" style="left:0;top:26px;width:406px;height:406px;background:linear-gradient(160deg,#545b64,#c3c9cf 55%,#8d949b)" role="img" aria-label="Single engine aircraft under repair in a hangar"></div>
</div>

<!-- school -->
<div class="ring" style="left:112px;top:2946px;width:432px;height:432px;background:linear-gradient(135deg,var(--navy),var(--blue))">
  <div class="photo" style="left:0;top:26px;width:406px;height:406px;background:linear-gradient(160deg,#3f4650,#9fb3c4 55%,#d5dde4)" role="img" aria-label="Pilot with headset seated at a cockpit's controls"></div>
</div>
<h2 class="heading abs" style="left:600px;top:2982px;font-size:40px">SCHOOL</h2>
<div class="abs" style="left:600px;top:3056px;width:489px">
  <p class="para">Lorem ipsum dolor sit amet, consectetur adipiscing elit, sed do eiusmod tempor incididunt ut labore et dolore magna aliqua. Ut enim ad minim veniam, quis nostrud exercitation ullamco laboris nisi ut aliquip ex ea commodo conseute irure dolor in reprehea.</p>
  <p class="para">Consectetur adipiscing elit, sed do eiusmod tempor incididunt ut labore et dolore magna aliqua ut enim ad minim veniam, quis nostrud exer citation ullamco laboris nisi ut aliquip exea.</p>
</div>
<div class="btn" style="left:600px;top:3285px;width:134px;height:45px">Learn More</div>

<!-- footer -->
<svg class="abs" style="left:0;top:3440px" width="1200" height="100" viewBox="0 0 1200 100">
  <path d="M0,112 L0,115 C150,20 300,15 520,55 C760,100 1000,95 1200,28 L1200,100 L0,100Z" fill="#272727"/>
  <path d="M0,115 C150,20 300,15 520,55 C760,100 1000,95 1200,28" fill="none" stroke="#0a8fd2" stroke-width="8"/>
  <path d="M30,94 C200,25 340,25 560,70 C800,110 1000,95 1200,45" fill="none" stroke="#1c3883" stroke-width="5"/>
</svg>
<footer class="abs footer"></footer>

<div class="abs" style="left:112px;top:3732px;width:176px;text-align:center">
  <div style="width:46px;height:46px;border-radius:50%;background:var(--grad);margin:0 auto 12px"></div>
  <div style="font-family:'Montserrat',sans-serif;font-weight:800;font-size:29px;color:#fff;letter-spacing:.5px">SKYLARK</div>
  <div style="font-family:'Montserrat',sans-serif;font-size:10px;letter-spacing:5px;color:#bbb;margin-top:2px">AVIATION</div>
</div>

<div class="foot-title" style="left:342px">QUICK LINKS</div>
<div class="foot-link" style="top:3683px"><i class="dot"></i>Home</div>
<div class="foot-link" style="top:3722px"><i class="dot"></i>About Us</div>
<div class="foot-link" style="top:3761px"><i class="dot"></i>Our Services</div>
<div class="foot-link" style="top:3801px"><i class="dot"></i>Contact Us</div>
<div class="foot-link" style="top:3839px"><i class="dot"></i>Privacy Policy</div>

<div class="foot-title" style="left:563px">CONTACT INFO</div>
<svg class="abs" style="left:563px;top:3683px" width="12" height="14" viewBox="0 0 12 14"><path d="M6 0a5 5 0 0 0-5 5c0 4 5 9 5 9s5-5 5-9a5 5 0 0 0-5-5z" fill="#0a8fd2"/></svg>
<div class="info" style="left:601px;top:3683px"><b>ADDRESS:</b>212 Hangar Row, Lawrenceville,<br>GA, United States</div>
<svg class="abs" style="left:563px;top:3762px" width="13" height="13" viewBox="0 0 13 13"><path d="M2 1l3 0 1 3-2 1a7 7 0 0 0 4 4l1-2 3 1v3c-6 0-10-4-10-10z" fill="#0a8fd2"/></svg>
<div class="info" style="left:601px;top:3762px"><b>PHONE:</b>+1 (555) 014 2280</div>
<svg class="abs" style="left:563px;top:3824px" width="14" height="10" viewBox="0 0 14 10"><rect width="14" height="10" rx="1" fill="#0a8fd2"/><path d="M0 0l7 5 7-5" fill="none" stroke="#272727" stroke-width="1.2"/></svg>
<div class="info" style="left:601px;top:3823px"><b>EMAIL:</b>info@skylarkairworks.com</div>

<div class="foot-title" style="left:801px">GET IN TOUCH</div>
<p class="abs" style="left:801px;top:3680px;width:287px;font-size:13px;line-height:23px;color:#eee;font-weight:500;text-align:justify">Lorem ipsum dolor sit amet, consectetur adip iscing elit, sed do eiusmod tempor incidid unt ut labore et dolore magna aliqua. Ut enim ad minim veniam, quis nostrud exercitea.</p>
<div class="btn" style="left:801px;top:3796px;width:134px;height:45px">Contact Us</div>

<div class="abs" style="left:112px;top:3895px;width:976px;height:1px;background:#4a4a4a"></div>
<div class="abs" style="left:450px;top:3917px;font-size:12px;color:#ddd">&copy; 2023 <b style="color:#fff">SKYLARK AVIATION</b> &nbsp;| &nbsp;All Rights Reserved</div>
<div class="social" style="left:970px;top:3907px">
  <span style="background:var(--blue);border-color:var(--blue);color:#fff">N</span>
  <span style="background:#fff;border-color:#fff">C</span>
  <span style="background:#fff;border-color:#fff">W</span>
</div>

</body>
</html>
```